Letterhead design for ZENTORA company

I need an A4 letterhead design for my company "Zentora Electrical Products". I need the letterhead to match my current logo and business card designs. I would like it to be colourful and match the design of the business card in terms of the flowing line of colour where the information is.  

Target Market(s)

Adults aged 20 - 50 Upper middle class.

Industry/Entity Type

It Company

Requirements
Must have
• Must be A4 size and match my current logo and business card designs. Must be clean simple and eye catching.

• Must have the following information

• Zentora Electrical Products LTD
• 7 Ardley Close
• Chiswick
• London
• England
• W9 3QX
• Company No. 05316429
• VAT No. GB 627150384

• Telephone: 02081594360
• Mobile: 07815062247
• Email: info@zentora-goods.co.uk
Nice to have
• nice to have a wave of colour like the business card.
Should not have
• Should not be a different colour scheme to the business card and logo design.

```html
<!DOCTYPE html>
<html lang="en">
<head>
<meta charset="UTF-8">
<title>Zentora Electrical Products – Letterhead</title>
<link href="https://fonts.googleapis.com/css2?family=Questrial&family=Open+Sans:wght@400&display=swap" rel="stylesheet">
<style>
  :root {
    --backdrop: #5f5f5f;
    --paper: #ffffff;
    --paper-edge: #e4e5e7;
    --brand: #0a8fb8;
    --brand-deep: #0075a0;
    --brand-light: #8fd6f2;
    --brand-mid: #1aa6cf;
    --ink: #2b2b2b;
    --white: #ffffff;
  }
  * { margin: 0; padding: 0; box-sizing: border-box; }
  html, body {
    width: 1200px; height: 998px; overflow: hidden;
    background: var(--backdrop);
  }
  .canvas {
    position: relative; width: 1200px; height: 998px;
    background: radial-gradient(ellipse at 50% 40%, #6e6e6e 0%, var(--backdrop) 70%);
  }
  .sheet {
    position: absolute; top: 95px; width: 529px; height: 749px;
    box-shadow: 0 4px 14px rgba(0,0,0,.35);
    overflow: hidden;
  }
  .letterhead-front {
    left: 58px;
    background: radial-gradient(ellipse at 50% 55%, var(--paper) 35%, var(--paper-edge) 100%);
  }
  .letterhead-back {
    left: 613px;
    background: radial-gradient(ellipse at 50% 55%, #5cc6e8 0%, #1ea5cf 40%, #0089b3 80%, #007aa3 100%);
  }
  .sheet svg.swoosh { position: absolute; inset: 0; width: 100%; height: 100%; }

  .brand-mark {
    position: absolute; left: 44px; top: 46px;
    font-family: "Questrial", sans-serif; color: var(--brand);
    line-height: 1;
  }
  .brand-mark .brand-name { font-size: 30px; letter-spacing: 1px; display: block; }
  .brand-mark .brand-line { font-size: 11.5px; letter-spacing: .4px; display: block; margin-top: 3px; }

  .contact-block, .registration-block {
    position: absolute; right: 25px; text-align: right;
    font-family: "Open Sans", sans-serif; font-size: 7px; line-height: 10.6px;
    color: var(--ink);
  }
  .contact-block { top: 27px; }
  .contact-block .company { color: var(--brand); }
  .contact-block .gap { height: 5px; }
  .label { color: var(--brand); }
  .registration-block { top: 712px; font-size: 6px; line-height: 8.6px; }

  .back-mark {
    position: absolute; left: 0; right: 0; top: 335px; text-align: center;
    font-family: "Questrial", sans-serif; color: var(--white); line-height: 1;
  }
  .back-mark .brand-name { font-size: 46px; letter-spacing: 1.5px; display: block; }
  .back-mark .brand-line { font-size: 17px; letter-spacing: 1px; display: block; margin-top: 4px; }
</style>
</head>
<body>
<main class="canvas">

  <section class="sheet letterhead-front" aria-label="Letterhead front">
    <svg class="swoosh" viewBox="0 0 529 749" aria-hidden="true">
      <defs>
        <linearGradient id="bandTop" x1="0" y1="0" x2="1" y2="1">
          <stop offset="0" stop-color="var(--brand-deep)"/>
          <stop offset="1" stop-color="var(--brand-mid)"/>
        </linearGradient>
      </defs>
      <path d="M168 0 C 240 95, 380 148, 529 156 L529 124 C 395 122, 275 78, 198 0 Z" fill="url(#bandTop)"/>
      <path d="M198 0 C 275 78, 395 122, 529 124 L529 128 C 420 126, 300 90, 220 0 Z" fill="var(--brand-light)"/>
      <path d="M327 749 C 382 708, 452 678, 529 668 L529 686 C 462 692, 402 720, 364 749 Z" fill="url(#bandTop)"/>
      <path d="M364 749 C 402 720, 462 692, 529 686 L529 690 C 470 698, 418 722, 378 749 Z" fill="var(--brand-light)"/>
    </svg>

    <div class="brand-mark">
      <span class="brand-name">ZENTORA</span>
      <span class="brand-line">Electrical Products</span>
    </div>

    <address class="contact-block" style="font-style:normal">
      <div class="company">Zentora Electrical Products LTD</div>
      <div>7 Ardley Close, Chiswick,</div>
      <div>London, England&nbsp; W9 3QX</div>
      <div class="gap"></div>
      <div><span class="label">P.</span> 02081594360&nbsp; <span class="label">M.</span> 07815062247</div>
      <div><span class="label">E.</span> info@zentora-goods.co.uk</div>
      <div><span class="label">W.</span> www.zentora-goods.co.uk</div>
    </address>

    <div class="registration-block">
      <div><span class="label">Company No.</span> 05316429</div>
      <div><span class="label">VAT No.</span> GB 627150384</div>
    </div>
  </section>

  <section class="sheet letterhead-back" aria-label="Letterhead optional back">
    <svg class="swoosh" viewBox="0 0 529 749" aria-hidden="true">
      <path d="M0 345 C 140 330, 260 360, 360 375 C 430 385, 490 340, 529 310 L529 560 C 470 470, 380 420, 270 400 C 170 385, 80 390, 0 400 Z" fill="rgba(255,255,255,0.10)"/>
      <path d="M0 345 C 140 330, 260 360, 360 375 C 430 385, 490 340, 529 310" fill="none" stroke="rgba(255,255,255,0.18)" stroke-width="1.5"/>
    </svg>
    <div class="back-mark">
      <span class="brand-name">ZENTORA</span>
      <span class="brand-line">Electrical Products</span>
    </div>
  </section>

</main>
</body>
</html>
```